Electrical Contractors Business Card Design

I need a business card design for an electrical contracting business. A theme I was thinking of is the PP of Pellworth Electrical both facing each other ie the second E is back to front and maybe each horizontal part of the E's are a different colours of the internal wires of TPS cable. The top would be blue(representing the sky), the middle green(representing the grass) and the lower would be brown(representing below the earth) (neutral,earth and active). And coming out of the back of each E going to each side of the business card would be the white outer sheath of TPS cable. I would like a big part of the card to be a very bright emerald flourescent green and maybe silver for the top half. the message I would like to send is that of an environmentally friendly, ethical business that delivers quality sevice on time.

Target Market(s)

40 to 80 year old home owners

Industry/Entity Type

Electrical

Contact Information for Business Card

Ned Calloway
Pellworth Electrical
EC 047382
Mob: 0451 876 293

```html
<!DOCTYPE html>
<html lang="en">
<head>
<meta charset="utf-8">
<title>Pellworth Electrical – Business Card</title>
<link rel="stylesheet" href="https://fonts.googleapis.com/css2?family=Public+Sans:wght@400;600&display=swap">
<style>
  :root {
    --page: #ffffff;
    --silver: #ececec;
    --sheath: #ffffff;
    --emerald: #559a75;
    --active-blue: #1f6fb8;
    --ink-light: #ffffff;
  }
  html, body {
    margin: 0;
    width: 1200px;
    height: 900px;
    overflow: hidden;
    background: var(--page);
    font-family: "Public Sans", Arial, sans-serif;
  }
  .card {
    position: absolute;
    left: 65px;
    top: 117px;
    width: 1075px;
    height: 650px;
    overflow: hidden;
    background: var(--emerald);
  }
  .card__silver {
    position: absolute;
    inset: 0 0 auto 0;
    height: 230px;
    background: var(--silver);
  }
  .card__sheath {
    position: absolute;
    left: 0;
    right: 0;
    top: 230px;
    height: 45px;
    background: var(--sheath);
  }
  .card__name {
    position: absolute;
    left: 150px;
    top: 108px;
    margin: 0;
    font-weight: 600;
    font-size: 84px;
    line-height: 88px;
    letter-spacing: 0;
    color: var(--emerald);
  }
  .card__name span { display: block; }
  .brand-mark {
    position: absolute;
    left: 690px;
    top: 140px;
    display: flex;
    align-items: center;
    gap: 18px;
  }
  .brand-mark__square {
    width: 46px;
    height: 46px;
    background: var(--active-blue);
  }
  .brand-mark__text {
    font-weight: 600;
    font-size: 80px;
    line-height: 1;
    color: var(--active-blue);
  }
  .card__contact {
    position: absolute;
    left: 0;
    right: 0;
    top: 534px;
    margin: 0;
    text-align: center;
    font-weight: 400;
    font-size: 40px;
    letter-spacing: 0.5px;
    color: var(--ink-light);
  }
</style>
</head>
<body>
  <main class="card">
    <div class="card__silver"></div>
    <div class="card__sheath"></div>
    <h1 class="card__name"><span>Pellworth</span><span>Electrical</span></h1>
    <div class="brand-mark">
      <div class="brand-mark__square"></div>
      <div class="brand-mark__text">PP</div>
    </div>
    <p class="card__contact">Ned Calloway | EC 047382 | Mob: 0451 876 293</p>
  </main>
</body>
</html>
```